Create New Bussiness Card For New Shoes Store

Vandrule is a store that sells a variety of skateboard shoes such as Kestro, Mollen etc. we also sell some skateboard and all skateboard accessories.
we like black and white style logo, but also like blue as well.
We are fully assembled with a deck, truck, wheels, and bearings. Add some personality to your board with a fun, graphic skateboard deck. Constructed of thick 7 ply maple,
Target Market(s)
Target audience: 12-40 year old
especially for young man
Industry/Entity Type
Industrial
Contact Information for Business Card
Name: Vandrule
Address1: 2483 Harlow Brisket Rd
City: Calvesta
State: Norland
Zip: 40719
Country: US
Phone: 614830296
email: markolvenby@plimmail.test

```html
<!DOCTYPE html>
<html lang="en">
<head>
<meta charset="utf-8">
<title>Vandrule – Business Card</title>
<link rel="stylesheet" href="https://fonts.googleapis.com/css2?family=Open+Sans:wght@300;400&display=swap">
<style>
  :root {
    --stage: #e4e2df;
    --card-shadow: rgba(0, 0, 0, 0.35);
    --sky-dark: #1c1c1c;
    --sky-mid: #4a4a4a;
    --sky-light: #8a8a8a;
    --ground: #111111;
    --ink: #ffffff;
  }
  * { box-sizing: border-box; margin: 0; padding: 0; }
  html, body {
    width: 1200px;
    height: 1000px;
    overflow: hidden;
    background: var(--stage);
  }
  .business-card {
    position: absolute;
    left: 270px;
    top: 307px;
    width: 660px;
    height: 386px;
    border-radius: 12px;
    overflow: hidden;
    box-shadow: 0 8px 18px var(--card-shadow);
    font-family: "Open Sans", sans-serif;
    color: var(--ink);
  }
  .card-photo {
    position: absolute;
    inset: 0;
    background:
      radial-gradient(ellipse 60% 70% at 72% 35%, var(--sky-light) 0%, transparent 70%),
      radial-gradient(ellipse 70% 60% at 20% 75%, var(--sky-mid) 0%, transparent 75%),
      linear-gradient(180deg, var(--sky-dark) 0%, var(--sky-mid) 55%, var(--ground) 100%);
  }
  .brand {
    position: absolute;
    left: 0;
    right: 0;
    top: 146px;
    display: flex;
    justify-content: center;
    align-items: center;
    gap: 12px;
  }
  .brand-name {
    font-weight: 300;
    font-size: 60px;
    line-height: 1;
    letter-spacing: 1px;
  }
  .brand-dot {
    width: 12px;
    height: 12px;
    border-radius: 50%;
    background: var(--ink);
  }
  .contact-line {
    position: absolute;
    left: 74px;
    top: 322px;
    display: flex;
    align-items: center;
    font-weight: 400;
    font-size: 16px;
    line-height: 20px;
    white-space: nowrap;
  }
  .contact-phone {
    display: flex;
    align-items: center;
    gap: 6px;
    margin-left: 26px;
  }
  .phone-icon { width: 20px; height: 20px; }
</style>
</head>
<body>
  <div class="business-card">
    <div class="card-photo" role="img" aria-label="Black and white photo of a skateboarder mid-air against a cloudy sky above a dark ramp"></div>

    <div class="brand">
      <span class="brand-name">Vandrule</span>
      <span class="brand-dot"></span>
    </div>

    <div class="contact-line">
      <span class="contact-address">2483 Harlow Brisket Rd, Calvesta, Norland 40719, US</span>
      <span class="contact-phone">
        <svg class="phone-icon" viewBox="0 0 20 20" aria-hidden="true">
          <circle cx="10" cy="10" r="9" fill="none" stroke="#ffffff" stroke-width="1.2"/>
          <path d="M7.2 5.2c.5-.3 1 0 1.2.4l.7 1.6c.2.4 0 .8-.3 1l-.6.5c.4 1 1.2 2 2.2 2.7l.6-.5c.3-.3.8-.3 1.1 0l1.4 1c.4.3.5.8.2 1.2l-.6.8c-.4.5-1.1.7-1.7.4-2.6-1.2-4.4-3.4-5.2-6.1-.2-.6 0-1.3.6-1.7z" fill="#ffffff"/>
        </svg>
        <span class="phone-number">614830296</span>
      </span>
    </div>
  </div>
</body>
</html>
```